Web Design Project for NCYB

Hi,
I am looking for a website design for the Northern Council for Youth Boards.
This is an organisation which helps with legal disputes and other challenges which involve children.  The company want a web page which is professional but friendly.  The purpose of the website is to explain what the organisation does and to give people a place where they can download documents and information.
The homepage will have a video on the page.  ALSO, we would prefer the site to have a left hand navigation (not a top navigation).
I have enclosed the logo, a picture of the old (rubbish) home page and a screenshot from the video (you are welcome to change the dimensions).
If you have any questions, please ask.
-K
UPDATE: 6th DECEMBER:
Thanks for the designs so far.  I promise to give feedback to every single person.  In the meantime, can I just say that there's some good designs so far but I don't think anyone has nailed this yet.
So, I am uploading a screenshot called "theylikethis.jpg".  This is a screenshot from a website that the client says they like.
Can I also say, it's okay to reduce the size of the video.  I'm seeing a lot of massive videos.
Thanks folks!
UPDATE:  You can view a live demo of the site that they like at www.demohostqz.co.uk
UPDATE:  I've just found another good example of a site with a left nav at www.brightresourcehubnet.com

Hi,
Hi folks,
Had a quick look at the designs and just to say how impressed I am with the qualityand choice. There are a few that caught my eye and I'll try and narrow them down.I've also passed the link onto the other representatives for their input beforemaking a final choice. If I don't hear from any of the other represenatatives by Wednesday, I'll chose adesign and let you know. Once again many thanks for the quick response in gettingdesigns done and really looking forward to seeing the completed website.
Industry/Entity Type
Legal
Requirements
Must have
- a video player (any size of your choosing)
a left side navigation
the logo

```html
<!DOCTYPE html>
<html lang="en">
<head>
<meta charset="utf-8">
<title>NCYB – Northern Council for Youth Boards</title>
<link href="https://fonts.googleapis.com/css2?family=Open+Sans:wght@400;600;700&family=PT+Sans+Narrow:wght@400;700&display=swap" rel="stylesheet">
<style>
:root{
  --navy:#0b3a8c;
  --nav-dark:#15284a;
  --nav-mid:#22406e;
  --brown:#6b3410;
  --stone:#e4e0d8;
  --stone-dark:#cfc9bd;
  --ink:#555;
  --ink-soft:#8a8a8a;
  --panel:#efefef;
  --white:#fff;
}
*{margin:0;padding:0;box-sizing:border-box}
html,body{width:1168px;height:1200px;overflow:hidden;background:var(--white)}
body{font-family:"Open Sans",Arial,sans-serif;color:var(--ink)}
.canvas{position:relative;width:1168px;height:1200px;overflow:hidden}
.stage{position:absolute;left:0;top:0;width:1020px;height:1048px;transform:scale(1.1451);transform-origin:0 0;overflow:hidden}
.abs{position:absolute}

/* header */
.site-header{left:0;top:0;width:1020px;height:98px;background:linear-gradient(180deg,#ebe8e1,var(--stone) 70%,var(--stone-dark))}
.dotted-edge{left:0;width:1020px;height:6px;background:radial-gradient(circle at 3px 3px,#8d877c 1.4px,transparent 1.8px) 0 0/7px 6px}
.brand{left:60px;top:12px;width:250px;text-align:center}
.brand-name{display:inline-flex;align-items:center;gap:6px;font-weight:700;font-size:30px;color:var(--navy);letter-spacing:1px;line-height:1}
.brand-dot{width:12px;height:12px;border-radius:50%;background:var(--navy)}
.brand-sub{margin-top:22px;font-size:10px;color:#444;letter-spacing:.2px;white-space:nowrap}
.enquiry{left:507px;top:20px}
.enquiry-label{display:flex;align-items:center;gap:8px;font-size:14px;color:#555}
.enquiry-number{font-size:31px;font-weight:700;color:#6e6e6e;line-height:1;margin-top:1px}
.search{left:728px;top:35px;display:flex;height:30px}
.search-field{width:178px;background:#fbfaf6;border:1px solid #d8d4ca}
.search-button{width:79px;background:var(--brown);color:#f0e6de;font-size:12px;display:flex;align-items:center;justify-content:center;gap:4px}

/* hero */
.hero{left:0;top:98px;width:1020px;height:396px;background:linear-gradient(100deg,#bdb8b1 0%,#8e8a86 35%,#d9d6d1 60%,#e9e7e3 85%,#8f9c7e 100%)}
.side-nav{left:35px;top:98px;width:288px;height:396px;background:linear-gradient(90deg,var(--nav-mid),var(--nav-dark) 70%,#1a2a44)}
.side-nav ul{list-style:none;padding:20px 0 0 62px}
.side-nav li{font-family:"PT Sans Narrow",sans-serif;font-size:24px;color:var(--white);height:42px;line-height:36px;text-transform:uppercase;letter-spacing:-.5px}
.side-nav .is-current{display:inline-block;border-bottom:4px solid var(--brown);line-height:32px}
.caption{left:472px;top:228px;width:513px;height:176px;background:rgba(40,44,54,.8);padding:10px 20px 0 33px;overflow:hidden}
.caption h1{font-family:"PT Sans Narrow",sans-serif;font-weight:400;font-size:43px;color:var(--white);line-height:50px;white-space:nowrap;letter-spacing:-.5px}
.caption p{font-size:13px;line-height:24px;color:#e8e8e8;margin:4px 0 0 3px;letter-spacing:-.15px}
.btn{display:inline-block;background:var(--brown);color:#f3e9e0;font-size:16px;padding:5px 13px;margin:13px 0 0 3px}
.slide-arrow{top:265px;width:54px;height:54px;border-radius:50%;background:rgba(235,235,235,.85);display:flex;align-items:center;justify-content:center}

/* features */
.features{left:35px;top:494px;width:950px;height:382px;background:var(--panel)}
.feature{top:544px;width:215px}
.feature-media{width:211px;height:119px;display:flex;align-items:center;justify-content:center}
.feature h2{margin-top:18px;font-size:15px;font-weight:700;color:var(--navy);padding-bottom:5px;border-bottom:3px solid #cfcfcf;width:211px;white-space:nowrap;letter-spacing:-.3px}
.feature p{margin-top:14px;font-size:12.5px;line-height:24px;color:var(--ink-soft);width:220px}
.read-more{display:flex;align-items:center;gap:8px;font-size:12.5px;color:var(--brown)}

/* footer */
.site-footer{left:0;top:878px;width:1020px;height:126px;background:linear-gradient(180deg,var(--stone-dark),var(--stone) 40%,#ebe8e2)}
.footer-brand{left:95px;top:914px;display:flex;align-items:center;gap:5px;font-weight:700;font-size:26px;color:var(--white)}
.footer-brand .brand-dot{background:var(--white)}
.footer-links{left:224px;top:922px;font-size:12.5px;color:#666}
.copyright{left:0;width:1076px;top:976px;text-align:center;font-size:10px;color:#555}
</style>
</head>
<body>
<div class="canvas">
<div class="stage">
  <header class="abs site-header"></header>
  <div class="abs brand">
    <div class="brand-name"><span class="brand-dot"></span>NCYB</div>
    <div class="brand-sub">NORTHERN COUNCIL FOR YOUTH BOARDS</div>
  </div>
  <div class="abs enquiry">
    <div class="enquiry-label">
      <svg width="24" height="16" viewBox="0 0 24 16"><path d="M2 6c0-4 20-4 20 0v2h-5V6H7v2H2z M6 8h12l3 7H3z" fill="#666"/><circle cx="12" cy="11" r="2" fill="#ddd"/></svg>
      CALL US FOR ENQUIRIES
    </div>
    <div class="enquiry-number">555-010-2040</div>
  </div>
  <div class="abs search">
    <div class="search-field"></div>
    <div class="search-button">SEARCH
      <svg width="12" height="12" viewBox="0 0 12 12"><circle cx="5" cy="5" r="3.5" stroke="#fff" stroke-width="1.6" fill="none"/><path d="M7.5 7.5 11 11" stroke="#fff" stroke-width="2"/></svg>
    </div>
  </div>
  <div class="abs dotted-edge" style="top:94px"></div>

  <div class="abs hero" role="img" aria-label="Photo of a young person sitting alone in a school corridor"></div>
  <nav class="abs side-nav">
    <ul>
      <li><span class="is-current">Home</span></li>
      <li>About Us</li><li>News</li><li>Conferences</li><li>Minutes</li>
      <li>Annual Report</li><li>Archive</li><li>Contact Us</li><li>Links</li>
    </ul>
  </nav>
  <div class="abs caption">
    <h1>WHY WAS THE NCYB FORMED?</h1>
    <p>Lorem ipsum dolor sit amet, consectetur adipisicing elit, sed do eius-mod tempor incididunt ut labore et dolore magna aliqua. Ut enim ad</p>
    <span class="btn">READ MORE</span>
  </div>
  <div class="abs slide-arrow" style="left:8px"><svg width="12" height="14" viewBox="0 0 12 14"><path d="M8 2 3 7l5 5" stroke="#fff" stroke-width="2.5" fill="none"/></svg></div>
  <div class="abs slide-arrow" style="left:948px"><svg width="12" height="14" viewBox="0 0 12 14"><path d="M4 2l5 5-5 5" stroke="#fff" stroke-width="2.5" fill="none"/></svg></div>

  <section class="abs features"></section>
  <article class="abs feature" style="left:87px">
    <div class="feature-media" role="img" aria-label="Video still of a smiling child with an adult" style="background:linear-gradient(120deg,#7a6a55,#4f4a3e 50%,#8b9aa8)">
      <svg width="36" height="36" viewBox="0 0 36 36"><circle cx="18" cy="18" r="16" fill="rgba(255,255,255,.25)" stroke="#ddd" stroke-width="2"/><path d="M14 11l10 7-10 7z" fill="#eee"/></svg>
    </div>
    <h2>LEARN MORE ABOUT US</h2>
    <p>Lorem ipsum dolor sit amet, con-sectetur adipisicing elit, sed do eiumod tempor incididunt ut labor-</p>
    <span class="read-more">Read More <svg width="18" height="10" viewBox="0 0 18 10"><path d="M0 5h16M12 1l4 4-4 4" stroke="#6b3410" stroke-width="1.6" fill="none"/></svg></span>
  </article>
  <article class="abs feature" style="left:410px">
    <div class="feature-media" role="img" aria-label="Embossed megaphone illustration on grey paper" style="background:linear-gradient(180deg,#d4d3d0,#c9c8c4)"></div>
    <h2>IN THE NEWS AND EVENTS</h2>
    <p>Lorem ipsum dolor sit amet, con-sectetur adipisicing elit, sed do eiumod tempor incididunt ut labor-</p>
    <span class="read-more">Read More <svg width="18" height="10" viewBox="0 0 18 10"><path d="M0 5h16M12 1l4 4-4 4" stroke="#6b3410" stroke-width="1.6" fill="none"/></svg></span>
  </article>
  <article class="abs feature" style="left:718px">
    <div class="feature-media" style="background:linear-gradient(180deg,#d4d3d0,#c9c8c4)">
      <svg width="104" height="86" viewBox="0 0 104 86"><circle cx="52" cy="33" r="33" fill="#a8a7a3"/><path d="M45 14h14v18h10L52 50 35 32h10z" fill="#e4e3df"/><path d="M2 62v22h100V62h-6v14H8V62z" fill="#8e8d89"/></svg>
    </div>
    <h2>DOWNLOAD RESOURCES</h2>
    <p>Lorem ipsum dolor sit amet, con-sectetur adipisicing elit, sed do eiumod tempor incididunt ut labor-</p>
    <span class="read-more">Read More <svg width="18" height="10" viewBox="0 0 18 10"><path d="M0 5h16M12 1l4 4-4 4" stroke="#6b3410" stroke-width="1.6" fill="none"/></svg></span>
  </article>

  <footer class="abs site-footer"></footer>
  <div class="abs dotted-edge" style="top:874px"></div>
  <div class="abs footer-brand"><span class="brand-dot"></span>NCYB</div>
  <div class="abs footer-links">Home | About Us | News | Conferences| Minutes | &nbsp;Annual Report | Archive | Contact Us | Links</div>
  <div class="abs copyright">COPYRIGHT 2012 NCYB | privacy policy | terms &amp; conditions</div>
</div>
</div>
</body>
</html>
```